Dental Medical History Form - Content provided

Design a medical history form for a dental practice. Content is provided so all that is needed is the formatting to make it look great and easy to read.

"Patient Information" to include all information contained in top portion of the "Patient Medical History Form" docx file.

"Medical History" should follow the formatting and content of the "Exact Medical History" file as this is what the entry fields look like in our practice software and so we would like it to match.

1st page - Patient info, allergies, medications, antibiotics, joint replacement, pregnancy.

2nd page - Do you have, or have you had, any of the following? . . . . . . .
Updates

Project Deadline Extended Reason: Picked too short of a deadline to start (2 days) Added Monday, February 13, 2017

Target Market(s)

All ages but must be clear enough for elderly to read. Use as much space as possible to keep font size bigger yet keep to two pages

Industry/Entity Type

Dental

Font styles to use
Sans Serif

Requirements
Must have
• All content provided
• Our logo at the top (file provided)
• Century Gothic Font
• Limit to two pages

```html
<!DOCTYPE html>
<html lang="en">
<head>
<meta charset="utf-8">
<title>Harbourline Dental – Confidential Medical History</title>
<link rel="stylesheet" href="https://fonts.googleapis.com/css2?family=Didact+Gothic&display=swap">
<style>
:root{
  --backdrop:#eceae6;
  --paper:#ffffff;
  --ink:#231f20;
  --ink-soft:#3a3a3a;
  --frame:#a9a9a9;
  --field:#e6e6e6;
  --bar:#231f20;
  --bar-text:#ffffff;
}
*{box-sizing:border-box;margin:0;padding:0}
html,body{width:1200px;height:1000px;overflow:hidden}
body{background:var(--backdrop);font-family:"Didact Gothic","Century Gothic",sans-serif;color:var(--ink);position:relative}
.page{position:absolute;top:108px;width:555px;height:785px;background:var(--paper);box-shadow:0 2px 10px rgba(0,0,0,.18)}
.page--patient{left:37px}
.page--history{left:613px}
.page-frame{position:absolute;left:13px;top:15px;right:13px;bottom:13px;border:1px solid var(--frame);border-radius:28px}
.abs{position:absolute;line-height:12px;font-size:9px;white-space:nowrap}
.field{position:absolute;height:10px;background:var(--field)}
.box{display:inline-block;width:7px;height:7px;border:1px solid #555;margin-left:1px;vertical-align:-1px}

/* brand */
.brand{position:absolute;left:26px;top:30px;display:flex;align-items:center;gap:8px}
.brand-name{font-size:22px;line-height:26px;color:var(--ink-soft)}
.brand-dot{width:9px;height:9px;border:1px solid var(--ink-soft);border-radius:50%}
.practice-address{position:absolute;left:26px;top:70px;font-size:8px;line-height:10px}
.form-title{position:absolute;left:26px;top:114px;font-size:11px;letter-spacing:.2px}
.form-rule{position:absolute;left:25px;top:129px;width:505px;height:3px;background:var(--ink)}
.small-label{font-size:9px}
.section-heading{font-weight:bold;font-size:9.5px}

/* section bars */
.section-bar{position:absolute;left:25px;width:505px;height:14px;background:var(--bar);color:var(--bar-text);font-size:9.5px;line-height:14px;padding-left:6px}
.question{font-size:9.5px;font-weight:bold}
.question .opt{font-weight:normal}

/* page 2 */
.history-bar{position:absolute;left:28px;top:37px;width:237px;height:14px;background:var(--bar);color:var(--bar-text);font-size:9px;line-height:14px;font-weight:bold;padding-left:6px}
.q-group{position:absolute;font-size:8.5px}
.q-group h3{font-size:8.5px;font-weight:bold;line-height:11.2px}
.q-row{display:grid;grid-template-columns:var(--label-w) 36px 36px;line-height:11.2px;white-space:nowrap}
.col-left{left:35px;--label-w:168px}
.col-right{left:295px;--label-w:172px}
.q-row .tight{font-size:7.5px}
.sign-line{position:absolute;height:1px;background:#777}
.closing-note{position:absolute;left:0;right:0;top:728px;text-align:center;font-size:7px;font-style:italic;line-height:8px}
</style>
</head>
<body>

<!-- Page 1: patient details -->
<section class="page page--patient">
  <div class="page-frame"></div>

  <div class="brand"><span class="brand-name">Harbourline Dental</span><span class="brand-dot"></span></div>
  <p class="practice-address">Suite 4/118 Coastal Parade<br>Lindale NSW 2261<br>(02) 4000 1234</p>

  <h1 class="form-title">CONFIDENTIAL MEDICAL HISTORY</h1>
  <div class="form-rule"></div>

  <!-- personal details -->
  <span class="abs" style="left:26px;top:140px">Name:</span>
  <div class="field" style="left:60px;top:141px;width:76px"></div>
  <div class="field" style="left:139px;top:141px;width:60px"></div>
  <div class="field" style="left:201px;top:141px;width:67px"></div>
  <span class="abs" style="left:25px;top:154px">Title</span>
  <span class="abs" style="left:86px;top:154px">First</span>
  <span class="abs" style="left:148px;top:154px">Middle</span>
  <span class="abs" style="left:225px;top:154px">Last</span>

  <span class="abs" style="left:26px;top:173px">Address:</span>
  <div class="field" style="left:70px;top:174px;width:198px"></div>
  <span class="abs" style="left:26px;top:189px">DOB:</span>
  <div class="field" style="left:53px;top:190px;width:215px"></div>
  <span class="abs" style="left:26px;top:207px">Email Address:</span>
  <div class="field" style="left:96px;top:208px;width:172px"></div>

  <span class="abs" style="left:75px;top:241px;width:36px;text-align:right">Mobile:</span>
  <div class="field" style="left:113px;top:242px;width:155px"></div>
  <span class="abs" style="left:75px;top:259px;width:36px;text-align:right">Work:</span>
  <div class="field" style="left:113px;top:260px;width:155px"></div>
  <span class="abs" style="left:75px;top:276px;width:36px;text-align:right">Home:</span>
  <div class="field" style="left:113px;top:277px;width:155px"></div>

  <!-- general practitioner -->
  <span class="abs section-heading" style="left:285px;top:140px">GENERAL PRACTITIONER:</span>
  <span class="abs" style="left:285px;top:156px">Name:</span>
  <div class="field" style="left:318px;top:157px;width:212px"></div>
  <span class="abs" style="left:285px;top:169px">Practice Name:</span>
  <div class="field" style="left:358px;top:170px;width:172px"></div>
  <span class="abs" style="left:285px;top:192px">Do you have a health fund with dental cover? <b>Yes</b> &nbsp;or <b>No</b></span>
  <span class="abs" style="left:285px;top:204px">If so, what is the name of the fund?</span>
  <div class="field" style="left:285px;top:218px;width:245px"></div>
  <span class="abs" style="left:285px;top:231px">Fund Number?</span>
  <div class="field" style="left:352px;top:232px;width:178px"></div>
  <span class="abs" style="left:285px;top:247px">Priority Number on card: &nbsp;&nbsp;&nbsp;&nbsp;&nbsp;<b style="word-spacing:6px">0 1 2 3 4 5</b></span>
  <span class="abs" style="left:285px;top:261px">Occupation:</span>
  <div class="field" style="left:345px;top:262px;width:185px"></div>
  <span class="abs" style="left:285px;top:276px">Referred by:</span>
  <div class="field" style="left:345px;top:277px;width:185px"></div>

  <!-- allergies -->
  <div class="section-bar" style="top:318px">Please indicate if &nbsp;you are allergic to any of the following <span class="box" style="border-color:#fff"></span> ?</div>
  <span class="abs" style="left:31px;top:337px">Aspirin<span class="box"></span></span>
  <span class="abs" style="left:82px;top:337px">Codeine<span class="box"></span></span>
  <span class="abs" style="left:144px;top:337px">Penicillin<span class="box"></span></span>
  <span class="abs" style="left:204px;top:337px">Sulfites<span class="box"></span></span>
  <span class="abs" style="left:256px;top:337px">Latex<span class="box"></span></span>
  <span class="abs" style="left:304px;top:337px">Local<span class="box"></span></span>
  <span class="abs" style="left:352px;top:337px">Anaesthetic<span class="box"></span></span>
  <span class="abs" style="left:426px;top:337px">Lactose<span class="box"></span></span>
  <span class="abs" style="left:484px;top:337px">Nickel<span class="box"></span></span>
  <span class="abs" style="left:31px;top:356px">Other</span>
  <div class="field" style="left:58px;top:357px;width:472px"></div>

  <!-- medications -->
  <div class="section-bar" style="top:392px">Are you currently taking, or have ever taken, any of the following medication <span class="box" style="border-color:#fff"></span> ?</div>
  <span class="abs" style="left:31px;top:409px">Asthma inhaler <span class="box"></span></span>
  <span class="abs" style="left:133px;top:409px">Anti-epileptics <span class="box"></span></span>
  <span class="abs" style="left:232px;top:409px">Anti-depressants<span class="box"></span></span>
  <span class="abs" style="left:341px;top:409px">Blood Pressure <span class="box"></span></span>
  <span class="abs" style="left:440px;top:409px">Blood Thinners <span class="box"></span></span>
  <span class="abs" style="left:31px;top:428px">Bisphosphonates<span class="box"></span></span>
  <span class="abs" style="left:133px;top:428px">Chemotherapy<span class="box"></span></span>
  <span class="abs" style="left:232px;top:428px">Insulin<span class="box"></span></span>
  <span class="abs" style="left:327px;top:428px">Immunosuppressants<span class="box"></span></span>
  <span class="abs" style="left:440px;top:428px">Steroids<span class="box"></span></span>
  <span class="abs" style="left:31px;top:447px">Oral Contraceptive <span class="box"></span></span>
  <span class="abs" style="left:31px;top:469px">Other</span>
  <div class="field" style="left:58px;top:470px;width:472px"></div>

  <!-- medication details -->
  <div class="section-bar" style="top:496px">Please specify medication name, dose, and frequency where possible:</div>
  <div class="field" style="left:31px;top:518px;width:162px;height:12px"></div>
  <div class="field" style="left:198px;top:518px;width:161px;height:12px"></div>
  <div class="field" style="left:364px;top:518px;width:161px;height:12px"></div>
  <div class="field" style="left:31px;top:537px;width:162px;height:12px"></div>
  <div class="field" style="left:198px;top:537px;width:161px;height:12px"></div>
  <div class="field" style="left:364px;top:537px;width:161px;height:12px"></div>
  <div class="field" style="left:31px;top:556px;width:162px;height:12px"></div>
  <div class="field" style="left:198px;top:556px;width:161px;height:12px"></div>
  <div class="field" style="left:364px;top:556px;width:161px;height:12px"></div>

  <!-- further questions -->
  <span class="abs question" style="left:26px;top:580px">Do you require antibiotic cover? &nbsp;<span class="opt">Yes<span class="box"></span> &nbsp;No<span class="box"></span></span></span>
  <span class="abs question" style="left:26px;top:609px">Have you had a joint replacement? &nbsp;<span class="opt">Yes<span class="box"></span> &nbsp;No<span class="box"></span></span></span>
  <span class="abs question" style="left:26px;top:638px">Women:</span>
  <span class="abs question" style="left:26px;top:653px">Are you pregnant? &nbsp;&nbsp;<span class="opt">Possible<span class="box"></span> &nbsp;Yes<span class="box"></span> &nbsp;No<span class="box"></span></span></span>
  <span class="abs question" style="left:26px;top:682px">Breast Feeding? &nbsp;<span class="opt">Yes<span class="box"></span> &nbsp;No<span class="box"></span></span></span>

  <span class="abs question" style="right:25px;top:737px">PLEASE TURN OVER</span>
</section>

<!-- Page 2: medical history -->
<section class="page page--history">
  <div class="page-frame"></div>
  <div class="history-bar">Do you have, or have you had, any of the following?</div>

  <div class="q-group col-left" style="top:62px">
    <h3>Dental</h3>
    <div class="q-row"><span>Acid Reflux</span><span>Yes<span class="box"></span></span><span>No<span class="box"></span></span></div>
    <div class="q-row"><span>Bad Breath/Taste</span><span>Yes<span class="box"></span></span><span>No<span class="box"></span></span></div>
    <div class="q-row"><span>Bleeding/Swollen/Sore Gums</span><span>Yes<span class="box"></span></span><span>No<span class="box"></span></span></div>
    <div class="q-row"><span>Blisters/Ulcers in Mouth</span><span>Yes<span class="box"></span></span><span>No<span class="box"></span></span></div>
    <div class="q-row"><span>Broken tooth/filling</span><span>Yes<span class="box"></span></span><span>No<span class="box"></span></span></div>
    <div class="q-row"><span>Burning tongue</span><span>Yes<span class="box"></span></span><span>No<span class="box"></span></span></div>
    <div class="q-row"><span>Dry mouth</span><span>Yes<span class="box"></span></span><span>No<span class="box"></span></span></div>
    <div class="q-row"><span>Food collection between teeth</span><span>Yes<span class="box"></span></span><span>No<span class="box"></span></span></div>
    <div class="q-row"><span>Grinding/clenching teeth (day/night)</span><span>Yes<span class="box"></span></span><span>No<span class="box"></span></span></div>
    <div class="q-row"><span>Loose teeth</span><span>Yes<span class="box"></span></span><span>No<span class="box"></span></span></div>
    <div class="q-row"><span>Crooked teeth</span><span>Yes<span class="box"></span></span><span>No<span class="box"></span></span></div>
    <div class="q-row"><span>Discoloured teeth</span><span>Yes<span class="box"></span></span><span>No<span class="box"></span></span></div>
    <div class="q-row"><span>Sensitivity to Hot/Cold</span><span>Yes<span class="box"></span></span><span>No<span class="box"></span></span></div>
    <div class="q-row"><span>Tooth pain when chewing</span><span>Yes<span class="box"></span></span><span>No<span class="box"></span></span></div>
    <div class="q-row"><span>Jaw pain/Fracture</span><span>Yes<span class="box"></span></span><span>No<span class="box"></span></span></div>
    <div class="q-row"><span>Orthodontic treatment/history</span><span>Yes<span class="box"></span></span><span>No<span class="box"></span></span></div>
    <div class="q-row"><span>Oral Cancer</span><span>Yes<span class="box"></span></span><span>No<span class="box"></span></span></div>
  </div>

  <div class="q-group col-left" style="top:273px">
    <h3>Diet/Lifestyle</h3>
    <div class="q-row"><span class="tight">Drink more than one glass alcohol per day</span><span>Yes<span class="box"></span></span><span>No<span class="box"></span></span></div>
    <div class="q-row"><span>Smoking</span><span>Yes<span class="box"></span></span><span>No<span class="box"></span></span></div>
    <div class="q-row"><span>Carbonated drinks</span><span>Yes<span class="box"></span></span><span>No<span class="box"></span></span></div>
    <div class="q-row"><span>Sugary foods</span><span>Yes<span class="box"></span></span><span>No<span class="box"></span></span></div>
  </div>

  <div class="q-group col-left" style="top:340px">
    <h3>Blood</h3>
    <div class="q-row"><span>Anaemia</span><span>Yes<span class="box"></span></span><span>No<span class="box"></span></span></div>
    <div class="q-row"><span>Blood clots</span><span>Yes<span class="box"></span></span><span>No<span class="box"></span></span></div>
    <div class="q-row"><span>Leukemia</span><span>Yes<span class="box"></span></span><span>No<span class="box"></span></span></div>
    <div class="q-row"><span>Low platelets</span><span>Yes<span class="box"></span></span><span>No<span class="box"></span></span></div>
    <div class="q-row"><span>Lymphoma</span><span>Yes<span class="box"></span></span><span>No<span class="box"></span></span></div>
    <div class="q-row"><span>Haemophelia</span><span>Yes<span class="box"></span></span><span>No<span class="box"></span></span></div>
  </div>

  <div class="q-group col-left" style="top:430px">
    <h3>Chest</h3>
    <div class="q-row"><span>Bronchitis</span><span>Yes<span class="box"></span></span><span>No<span class="box"></span></span></div>
    <div class="q-row"><span>Cystic Fibrosis</span><span>Yes<span class="box"></span></span><span>No<span class="box"></span></span></div>
    <div class="q-row"><span>Emphysema</span><span>Yes<span class="box"></span></span><span>No<span class="box"></span></span></div>
    <div class="q-row"><span>Pneumonia</span><span>Yes<span class="box"></span></span><span>No<span class="box"></span></span></div>
  </div>

  <div class="q-group col-left" style="top:496px">
    <h3>Infectious Disease</h3>
    <div class="q-row"><span>Creutzfeldt-Jakob Disease</span><span>Yes<span class="box"></span></span><span>No<span class="box"></span></span></div>
    <div class="q-row"><span>Hepatitis A,B,C,D</span><span>Yes<span class="box"></span></span><span>No<span class="box"></span></span></div>
    <div class="q-row"><span>HIV/AIDS</span><span>Yes<span class="box"></span></span><span>No<span class="box"></span></span></div>
    <div class="q-row"><span>Influenza</span><span>Yes<span class="box"></span></span><span>No<span class="box"></span></span></div>
    <div class="q-row"><span>Shingles</span><span>Yes<span class="box"></span></span><span>No<span class="box"></span></span></div>
    <div class="q-row"><span>Tuberculosis</span><span>Yes<span class="box"></span></span><span>No<span class="box"></span></span></div>
  </div>

  <div class="q-group col-right" style="top:62px">
    <h3>Heart</h3>
    <div class="q-row"><span>Angina</span><span>Yes<span class="box"></span></span><span>No<span class="box"></span></span></div>
    <div class="q-row"><span>Atrial Fibrillation</span><span>Yes<span class="box"></span></span><span>No<span class="box"></span></span></div>
    <div class="q-row"><span>Blood Pressure (High/Low)</span><span>Yes<span class="box"></span></span><span>No<span class="box"></span></span></div>
    <div class="q-row"><span>Congenital Heart Disease</span><span>Yes<span class="box"></span></span><span>No<span class="box"></span></span></div>
    <div class="q-row"><span>Heart attack</span><span>Yes<span class="box"></span></span><span>No<span class="box"></span></span></div>
    <div class="q-row"><span>Heart murmur</span><span>Yes<span class="box"></span></span><span>No<span class="box"></span></span></div>
    <div class="q-row"><span>Heart surgery</span><span>Yes<span class="box"></span></span><span>No<span class="box"></span></span></div>
    <div class="q-row"><span>Heart valve replacement</span><span>Yes<span class="box"></span></span><span>No<span class="box"></span></span></div>
    <div class="q-row"><span>Infective endocarditis</span><span>Yes<span class="box"></span></span><span>No<span class="box"></span></span></div>
    <div class="q-row"><span>Rheumatic Heart Disease</span><span>Yes<span class="box"></span></span><span>No<span class="box"></span></span></div>
    <div class="q-row"><span>Pacemaker</span><span>Yes<span class="box"></span></span><span>No<span class="box"></span></span></div>
    <div class="q-row"><span>Stent</span><span>Yes<span class="box"></span></span><span>No<span class="box"></span></span></div>
  </div>

  <div class="q-group col-right" style="top:222px">
    <h3>Other</h3>
    <div class="q-row"><span>Anxiety/PTSD</span><span>Yes<span class="box"></span></span><span>No<span class="box"></span></span></div>
    <div class="q-row"><span>Arthritis</span><span>Yes<span class="box"></span></span><span>No<span class="box"></span></span></div>
    <div class="q-row"><span>Alzheimer's</span><span>Yes<span class="box"></span></span><span>No<span class="box"></span></span></div>
    <div class="q-row"><span>Asthma</span><span>Yes<span class="box"></span></span><span>No<span class="box"></span></span></div>
    <div class="q-row"><span>Anaphylaxis</span><span>Yes<span class="box"></span></span><span>No<span class="box"></span></span></div>
    <div class="q-row"><span>Auto-immune disease</span><span>Yes<span class="box"></span></span><span>No<span class="box"></span></span></div>
    <div class="q-row"><span>Coeliac</span><span>Yes<span class="box"></span></span><span>No<span class="box"></span></span></div>
    <div class="q-row"><span>Depression</span><span>Yes<span class="box"></span></span><span>No<span class="box"></span></span></div>
    <div class="q-row"><span>Diabetes</span><span>Yes<span class="box"></span></span><span>No<span class="box"></span></span></div>
    <div class="q-row"><span>Epilepsy</span><span>Yes<span class="box"></span></span><span>No<span class="box"></span></span></div>
    <div class="q-row"><span>Kidney Disease</span><span>Yes<span class="box"></span></span><span>No<span class="box"></span></span></div>
    <div class="q-row"><span>Liver Disease</span><span>Yes<span class="box"></span></span><span>No<span class="box"></span></span></div>
    <div class="q-row"><span>Osteoporosis</span><span>Yes<span class="box"></span></span><span>No<span class="box"></span></span></div>
    <div class="q-row"><span>Parkinson's</span><span>Yes<span class="box"></span></span><span>No<span class="box"></span></span></div>
    <div class="q-row"><span>Radiation to Head/Neck</span><span>Yes<span class="box"></span></span><span>No<span class="box"></span></span></div>
    <div class="q-row"><span>Schizophrenia</span><span>Yes<span class="box"></span></span><span>No<span class="box"></span></span></div>
    <div class="q-row"><span>Snoring</span><span>Yes<span class="box"></span></span><span>No<span class="box"></span></span></div>
    <div class="q-row"><span>Sleep apnea</span><span>Yes<span class="box"></span></span><span>No<span class="box"></span></span></div>
    <div class="q-row"><span>Stroke</span><span>Yes<span class="box"></span></span><span>No<span class="box"></span></span></div>
  </div>

  <span class="abs section-heading" style="left:295px;top:486px;font-size:8.5px">Other</span>
  <div class="field" style="left:295px;top:499px;width:232px;height:11px"></div>
  <div class="field" style="left:295px;top:516px;width:232px;height:11px"></div>
  <div class="field" style="left:295px;top:532px;width:232px;height:11px"></div>
  <div class="field" style="left:295px;top:549px;width:232px;height:11px"></div>
  <div class="field" style="left:295px;top:565px;width:232px;height:11px"></div>

  <span class="abs" style="left:35px;top:659px;font-size:8px">SIGNATURE</span>
  <div class="sign-line" style="left:85px;top:668px;width:175px"></div>
  <span class="abs" style="left:326px;top:659px;font-size:8px">DATE</span>
  <div class="sign-line" style="left:352px;top:668px;width:175px"></div>

  <p class="closing-note">Thank you for the time to complete your medical history form.<br>Oral health is linked to overall health and this comprehensive questionnaire will help us to provide you with optimal and safe care.</p>
</section>

</body>
</html>
```